Cloud Based Internet Protection Service Business Cards

I would like a professionally designed business card. I already have a logo which I have attached.

The business is an online cloud based internet protection service aimed parents, particularly at non-technical parents and also schools.

The card should be be quite simple in its design, not to full of text and give its information in a clear and concise manner

Target Market(s)

Parents (especially non-technical parents) and also schools

Industry/Entity Type

Internet

Colors

Designer to choose colors to be used in the design.

Requirements
Should not have
• Too much text or be too cluttered. No decorative fonts, just a clear and concise font.

```html
<!DOCTYPE html>
<html lang="en">
<head>
<meta charset="utf-8">
<title>Safewatch Cloud – Business Cards</title>
<link rel="stylesheet" href="https://fonts.googleapis.com/css2?family=Lato:wght@400;700&display=swap">
<style>
  :root {
    --backdrop: #8b5430;
    --card-dark: #1f1f20;
    --card-light: #ffffff;
    --mark-dark: #3b3b3d;
    --navy: #0d4a6e;
    --sky: #2a9bd4;
  }
  * { margin: 0; padding: 0; box-sizing: border-box; }
  html, body {
    width: 1200px; height: 800px; overflow: hidden;
    background: var(--backdrop);
    font-family: "Lato", Arial, sans-serif;
  }
  .canvas { position: relative; width: 1200px; height: 800px; }
  .card {
    position: absolute;
    border-radius: 14px;
    box-shadow: 0 3px 10px rgba(0,0,0,0.35);
  }
  .card--front {
    left: 260px; top: 94px; width: 514px; height: 316px;
    background: var(--card-dark);
    display: flex; align-items: center; justify-content: center;
  }
  .card--back {
    left: 264px; top: 425px; width: 507px; height: 313px;
    background: var(--card-light);
  }
  .brand {
    display: flex; align-items: center; gap: 12px;
    font-weight: 700; white-space: nowrap;
  }
  .brand__dot { border-radius: 50%; flex: none; }
  .card--front .brand { color: var(--mark-dark); font-size: 44px; }
  .card--front .brand__dot { width: 46px; height: 46px; background: var(--mark-dark); }
  .card--back .brand {
    position: absolute; left: 26px; top: 140px;
    color: var(--navy); font-size: 27px;
  }
  .card--back .brand__dot { width: 34px; height: 34px; background: var(--navy); }
  .person { position: absolute; left: 288px; top: 36px; }
  .person__name { color: var(--navy); font-size: 18px; font-weight: 700; line-height: 22px; }
  .person__role { color: var(--sky); font-size: 14px; line-height: 18px; }
  .contacts { position: absolute; left: 288px; top: 117px; list-style: none; }
  .contacts li {
    display: flex; align-items: center; gap: 6px;
    color: var(--sky); font-size: 12.5px; line-height: 19px;
  }
  .contacts svg { width: 13px; height: 13px; fill: var(--navy); flex: none; }
  .office { position: absolute; left: 289px; top: 230px; }
  .office__name { color: var(--navy); font-size: 14px; font-weight: 700; line-height: 20px; }
  .office__address { color: var(--sky); font-size: 12.5px; line-height: 19.5px; }
</style>
</head>
<body>
<main class="canvas">
  <section class="card card--front" aria-label="Card front">
    <div class="brand"><span class="brand__dot"></span>Safewatch Cloud</div>
  </section>

  <section class="card card--back" aria-label="Card back">
    <div class="brand"><span class="brand__dot"></span>Safewatch Cloud</div>

    <div class="person">
      <p class="person__name">Harper Lewis</p>
      <p class="person__role">President</p>
    </div>

    <ul class="contacts">
      <li>
        <svg viewBox="0 0 16 16" aria-hidden="true"><path d="M3.6 1.2l2.3 2.9-1.3 1.6c.9 2 2.5 3.6 4.6 4.6l1.6-1.3 2.9 2.3-1.4 2.4C7.5 13.3 2.7 8.5 1.2 3.7z"/></svg>
        123 555 0198
      </li>
      <li>
        <svg viewBox="0 0 16 16" aria-hidden="true"><path d="M4 1h8v4H4zM1 6h14v6h-3v3H4v-3H1zm4 4v4h6v-4z"/></svg>
        123 555 0199
      </li>
      <li>
        <svg viewBox="0 0 16 16" aria-hidden="true"><path d="M1 3h14v10H1zm1.5 1.2L8 8.6l5.5-4.4z"/></svg>
        harper.l@safewatchcloud.co.uk
      </li>
      <li>
        <svg viewBox="0 0 16 16" aria-hidden="true"><path d="M8 1a7 7 0 1 0 0 14A7 7 0 0 0 8 1zm0 1.5c.9 1.2 1.4 2.8 1.5 4.5h-3c.1-1.7.6-3.3 1.5-4.5zM2.6 7h2.4c.1-1.6.5-3 1.1-4.1A5.5 5.5 0 0 0 2.6 7zm0 2a5.5 5.5 0 0 0 3.5 4.1C5.5 12 5.1 10.6 5 9zm3.9 0h3c-.1 1.7-.6 3.3-1.5 4.5-.9-1.2-1.4-2.8-1.5-4.5zm4.5 0c-.1 1.6-.5 3-1.1 4.1A5.5 5.5 0 0 0 13.4 9zm2.4-2A5.5 5.5 0 0 0 9.9 2.9c.6 1.1 1 2.5 1.1 4.1z"/></svg>
        www.safewatchcloud.co.uk
      </li>
    </ul>

    <div class="office">
      <p class="office__name">Safewatch Cloud</p>
      <p class="office__address">Suite 118, St. 9, Elm Grove Road,<br>UK 54321</p>
    </div>
  </section>
</main>
</body>
</html>
```